ECサイトのブランドコンセプトページ、商品ページ、プロモーションページのデザインをおねがいします。HTMLコーディングは含みません。

基本的な掲載コンテンツに変更はありません。添付のワイヤーを基に、フラワーショップのスイーツ店らしいシンプルで上品なデザインを希望します。作成頂いたコンセプトページをベースに他のページも制作したいと考えているため、その点も考慮して下さい。ロゴは添付ファイルのものを利用ください。

・デバイスフォントはWin "小塚ゴシック"、Mac "ヒラギノゴシック"、色がアースカラー。
・ターゲットは、30代~50代。スイーツ、花などの贈り物の購入者や、女子会、ホームパーティーでの購入者を想定。
・配色、クリエイティブは、参考サイトを参照。
[参考サイト]
http://www.morvanette.jp/
http://www.tolvicane.co.jp/

サイトリリース時にデザインに手を加えることをご了承ください。

ご質問・ご確認事項ありましたら「この依頼に質問」からお願いします。
それではたくさんのご応募お待ちしております。
3ページ
アースカラー、ピンク、ホワイト、
選定後納品ファイルですが、レイヤー情報を保持した.ai,.psdのいずれかを納品いただきます。当方、Win版CS5。
情報が少なかったので追記致します。

商品ページは全ての商品に共通したデザイン・キャッチコピーをおねがいします。
商品ページのイメージは下記サイトを参考にお願いします。

http://www.zenkuro8.com/menu/premiumcheesetart/

プロモーションページは下記サイトのような特集を組んで商品ページに誘導するイメージです

http://www.dorimenasu.com/new.php?twn=327
たくさんのご提案ありがとうございました。

ただ今、選考中です。
今しばらくお待ちください。
選定にお時間をいただき申し訳ございません。
とても良い提案が多く、クライアントの方でも決めかねております。

現在、クライアントの方で当選候補者様を数名に絞っていただいてるのですが、クライアントから候補者様のデザインされたプロモーションページが見たいという要望がございまして、ご応募いただいたランサー様に大至急、プロモーションページのデザインをお願い致します。当選候補者様には個別で修正依頼として、お願いを致します。修正依頼のないランサー様には申し訳ございませんが、ご了承ください。

プロモーションページをご提案いただけた方の中から必ず当選者を選ばせて頂くことを確約致します。
ご対応いただいている皆様
要件急変、大変申し訳ございません。

クライアントの方でこんなイメージも見たい、あんなイメージも見たいと意見が二転三転しておりまして、あれもこれもと対応していただくわけにはいかないので、ナビの画像など無しで小さめのおしゃれなフォントにしていただくだけで構いません。
プロモーションのページについては下記参考サイトのような白背景にフォントと余白で魅せるデザインでお願いできないでしょうか?

レイアウトはワイヤーの通りで構いません。

参考:http://vetrune-online.com/

お手数おかけして申し訳ございませんが、何卒よろしくお願い致します。

急な変更にご対応いただいているランサー様。
ありがとうございます。

ご提案いただいた案は全て、クライアントに提示致します。
ご提案いただいた案の中から必ず当選者を確定することを約束致します。

当選者のランサー様には当選したデザイン案でのブランドコンセプトページ、
商品ページの修正をお願い致します。お手数ではございますが、何卒ご了承くださいますようよろしくお願い申し上げます。
急な変更にも関わらず、ご対応いただきましたランサーの皆様、ありがとうございます。

現在、ご提案いただいたプロモーションページのデザインをクライアントに提出し選定中でございます。

提出致しましたデザインの中から当選者様を選ばせて頂きます。

当選者様には、お手数ではございますが、当選デザインでの商品ページ、コンセプトページの修正をお願い致しますこと、ご了承くださいますようお願い申し上げます。
当選者様は決定しているのですが、まだ修整をお願いすることがございまして、当選の確定を控えさせていただいております。

ご提案を頂いたランサーの皆様がたには、当選の確定をお待たせしてしまっていることお詫び申し上げます。

シンプルな中にも品があり、クライアント様の受けもよく、度重なる修正のお願いにもご対応いただき、クライアント様のイメージに近づけることができました。ありがとうございます。

急な要件変更にも関わらず、ご対応いただきましたランサーの皆様、ありがとうございました。

```html
<!DOCTYPE html>
<html lang="ja">
<head>
<meta charset="utf-8">
<title>FLORETTE SWEETS | Concept</title>
<link rel="stylesheet" href="https://fonts.googleapis.com/css2?family=Noto+Sans+JP:wght@400;500;700&family=Noto+Serif+JP:wght@500;700&family=Cormorant+Garamond:ital,wght@0,500;1,500&display=swap">
<style>
:root{
  --brown-dark:#3a2a22;
  --brown:#5b4336;
  --brown-mid:#8a6d5a;
  --beige:#efe7dc;
  --beige-light:#f7f2ea;
  --pink:#c9465c;
  --rose-red:#b8223a;
  --text:#3d302a;
  --line:#d9cbbb;
  --white:#ffffff;
}
*{margin:0;padding:0;box-sizing:border-box}
html,body{width:1200px;height:2424px;overflow:hidden}
body{background:var(--white);color:var(--text);font-family:"Noto Sans JP",sans-serif;font-size:15px;line-height:1.9;position:relative}
.topbar{height:32px;background:var(--brown-dark);color:#d8cabb;font-size:11px;display:flex;align-items:center;justify-content:space-between;padding:0 24px}
.topbar .util{display:flex;gap:18px}
.header{height:136px;position:relative;display:flex;align-items:center;justify-content:center}
.header .roses-l,.header .roses-r{position:absolute;top:0;height:136px}
.header .roses-l{left:0;width:260px;background:linear-gradient(90deg,#b33548,#e8a9b2 60%,transparent)}
.header .roses-r{right:0;width:300px;background:linear-gradient(270deg,#c2344c,#eeb3bc 60%,transparent)}
.brand{display:flex;align-items:center;gap:14px;font-family:"Noto Sans JP",sans-serif;font-weight:500;font-size:30px;color:var(--brown);letter-spacing:6px}
.brand .mark{width:12px;height:12px;border-radius:50%;background:var(--brown)}
.nav{height:32px;margin:0 20px;background:var(--brown);display:flex;align-items:center;padding-left:140px}
.nav a{color:#eadfd3;text-decoration:none;font-family:"Cormorant Garamond",serif;font-size:15px;width:108px;text-align:center}
.nav a.current{color:var(--white);border-bottom:2px solid var(--pink)}
.nav .cart{margin-left:auto;width:140px;height:32px;background:var(--pink);color:#fff;display:flex;align-items:center;justify-content:center;font-family:"Cormorant Garamond",serif;letter-spacing:2px}
.page{display:grid;grid-template-columns:252px 880px;gap:28px;padding:32px 20px 0}
.side .menu{border:1px solid var(--line);background:var(--beige)}
.side .menu h2{font-family:"Cormorant Garamond",serif;font-size:19px;color:var(--brown);padding:8px 14px;border-bottom:1px solid var(--line);background:var(--beige-light)}
.side .menu li{list-style:none;display:flex;align-items:center;gap:10px;padding:7px 10px;border-bottom:1px dotted var(--line);height:52px}
.side .menu li span{width:40px;height:38px;background:linear-gradient(135deg,#e9d4c0,#c79f86)}
.side .menu li em{font-family:"Cormorant Garamond",serif;font-style:italic;font-size:17px;color:var(--brown-mid)}
.side .photo{margin-top:16px;height:296px}
.side .photo.cake{background:linear-gradient(160deg,#f5e6dc,#e7b7b0 55%,#d9c2ad)}
.side .photo.tea{height:320px;background:linear-gradient(160deg,#f0e4d8,#c55a66 50%,#eadbc8)}
.side .news{margin-top:16px;border:1px solid var(--line);height:240px}
.side .news h3{font-size:11px;background:var(--brown);color:#fff;padding:3px 10px;font-weight:500}
.side .news p{font-size:11px;padding:8px 10px;color:var(--brown-mid)}
.crumb{font-size:11px;color:var(--brown-mid);margin-bottom:6px}
.letter{height:812px;background:linear-gradient(180deg,#f9f4ee,#f3ebe2);border:1px solid var(--line);position:relative;padding:40px 70px}
.letter h1{font-family:"Noto Serif JP",serif;font-weight:500;font-size:38px;color:var(--brown);text-align:center;border-bottom:1px solid var(--brown-mid);padding-bottom:14px;margin:0 0 34px}
.letter p{font-size:15px;margin-bottom:22px;line-height:2}
.letter .flower{position:absolute;right:60px;bottom:90px;width:170px;height:120px;border-radius:50%;background:radial-gradient(circle,#e6768a,#f4d3d8 70%,transparent)}
.letter .sign{position:absolute;right:60px;bottom:40px;font-family:"Noto Serif JP",serif;font-weight:700;font-size:15px}
.section-title{margin-top:30px;text-align:center;font-family:"Noto Serif JP",serif;font-size:20px;color:var(--rose-red);border-top:1px solid var(--line);border-bottom:1px solid var(--line);padding:8px 0;font-weight:500}
.hero-photo{margin-top:20px;height:248px;background:linear-gradient(100deg,#c0293f,#e14a5d 40%,#b7a493 75%,#d9cfc4)}
.feature{display:grid;gap:32px;margin-top:32px;align-items:start}
.feature.right{grid-template-columns:1fr 328px}
.feature.left{grid-template-columns:328px 1fr}
.feature .img{height:232px}
.feature .img.field{background:linear-gradient(180deg,#c9d8c6,#b32a3e 45%,#5d7a4d)}
.feature .img.petals{background:linear-gradient(135deg,#8f2434,#d13d54 50%,#7a5b46)}
.feature h3,.history h3{font-family:"Noto Serif JP",serif;font-size:20px;color:var(--rose-red);font-weight:500;border-bottom:1px solid var(--line);padding-bottom:6px;margin-bottom:14px}
.feature p,.history p{font-size:14px}
.history{margin-top:40px}
.footer{position:absolute;left:0;right:0;bottom:0;height:36px;background:var(--brown-dark);color:#cbbcae;font-size:11px;display:flex;align-items:center;justify-content:flex-end;padding-right:24px}
</style>
</head>
<body>
<div class="topbar"><span>スイーツと花のお店です</span><div class="util"><span>Login</span><span>Member</span><span>Guide</span><span>Contact</span><span>Sitemap</span></div></div>
<header class="header">
  <div class="roses-l" role="img" aria-label="赤いバラの写真"></div>
  <div class="brand"><span class="mark"></span>FLORETTE SWEETS</div>
  <div class="roses-r" role="img" aria-label="ピンクと赤のバラの写真"></div>
</header>
<nav class="nav">
  <a>Home</a><a class="current">Concept</a><a>Product</a><a>Promotion</a><a>Media</a><a>Policy</a><a>Login</a>
  <span class="cart">CART</span>
</nav>
<div class="page">
  <aside class="side">
    <div class="menu">
      <h2>Product</h2>
      <ul>
        <li><span role="img" aria-label="ロールケーキの写真"></span><em>Roll cake</em></li>
        <li><span role="img" aria-label="シュータルトの写真"></span><em>Choux tart</em></li>
        <li><span role="img" aria-label="フィナンシェの写真"></span><em>Financier</em></li>
        <li><span role="img" aria-label="ラスクの写真"></span><em>Rusk cake</em></li>
        <li><span role="img" aria-label="クッキーの写真"></span><em>Cookie of rose</em></li>
        <li><span role="img" aria-label="マカロンの写真"></span><em>Macaron</em></li>
        <li><span role="img" aria-label="ガトーの写真"></span><em>Gateau</em></li>
      </ul>
    </div>
    <div class="photo cake" role="img" aria-label="バラを添えたケーキの写真"></div>
    <div class="photo tea" role="img" aria-label="バラの花びらと紅茶の写真"></div>
    <div class="news"><h3>営業日カレンダー</h3><p>毎週水曜日は定休日です。</p></div>
  </aside>
  <main>
    <div class="crumb">Top &gt; Concept</div>
    <section class="letter">
      <h1>お客様へ</h1>
      <p>私たちは花屋だからこそ、ギフトやウェディングなど、さまざまなシーンで感動の演出をお手伝い申し上げております。<br>その中から「お花の魅力をお伝えしたい！」「お客様に喜びとサプライズをお届けしたい！」という気持ちから生まれてまいりました。</p>
      <p>そして FLORETTE SWEETS を立ち上げました。<br>ギフトとして受け取った方がパッと笑顔になっていただける！<br>お召し上がりいただいた方のこころに一輪の花が咲くようにとの願いを込めて。<br>特別なひとときに特別な気持ちをお届けします。<br>こころもカラダもキレイになる！</p>
      <p><strong>こんなことを願って心を込めて作りました。<br>一輪一輪ていねいに、ひとつひとつに心を込めて。</strong></p>
      <p><strong>今後とも宜しくご愛顧下さいますようお願い申し上げます。</strong></p>
      <div class="flower" role="img" aria-label="バラの花束のイラスト"></div>
      <div class="sign">株式会社 KM花工房</div>
    </section>
    <h2 class="section-title">素材へのこだわり</h2>
    <div class="hero-photo" role="img" aria-label="両手いっぱいのバラの花びらの写真"></div>
    <section class="feature right">
      <div>
        <h3>忘れられない薔薇を作る</h3>
        <p>森川薔薇園は、「忘れられない薔薇を作る」を合言葉に、自然なバラの無農薬栽培を手掛けてきました。<br>FLORETTE SWEETS の多くは、森川薔薇園のバラを使用しています。</p>
      </div>
      <div class="img field" role="img" aria-label="バラ園の写真"></div>
    </section>
    <section class="feature left">
      <div class="img petals" role="img" aria-label="摘み取ったバラの花びらの写真"></div>
      <div>
        <h3>紅雅は、森川薔薇園のオリジナルローズ</h3>
        <p>香りのバラ「紅雅」は、濃厚な芳香性と深紅の色、花弁の肉厚さが特徴。<br>10年の品種、栽培技術の研究開発を経て作られた森川薔薇園の生み出したオリジナルブランドローズです。<br>感動する香りと色彩、それが「紅雅」です。</p>
      </div>
    </section>
    <section class="history">
      <h3>実は、日本でも古くからバラを観賞用以外に活用されていました。</h3>
      <p>実は、日本でも古くからバラを観賞用以外に活用されていました。江戸時代の外科医学書にはバラの薬効が記され、花から蒸留した香り高いローズウォーターも用いられていたと伝えられています。</p>
    </section>
  </main>
</div>
<footer class="footer">Copyright © FLORETTE SWEETS All Rights Reserved.</footer>
</body>
</html>
```